Spa needs a storefront sticker design

For our city spa we need window stickers for the shop window.
The window stickers must fill the entire windows.
What we have in mind is that our logo is visible in the middle with graphic shapes surrounding it to stand out extra on the main street. The design is going to be printed in white and cut out. To give an impression of what we have in mind, our logo is attached with various example designs.
please supply your final file in the following extensions: – Eps file (*.eps) – Photoshop file (*.psd) – Adobe Portable Document (*.pdf) – Jpeg file ( *.jpg, *.jpeg) – Tiff file (*.tif, *.tiff)– Text in letter outlines
A photo of the shop window will be added tomorrow, including the exact dimensions so that the design can be adjusted accordingly
Look and feel
Each slider illustrates characteristics of the customer's brand and the style your logo design should communicate.

```html
<!DOCTYPE html>
<html lang="en">
<head>
<meta charset="utf-8">
<title>Linden – Storefront Window Sticker</title>
<link href="https://fonts.googleapis.com/css2?family=Marcellus&display=swap" rel="stylesheet">
<style>
  :root {
    --ink-black: #000000;
    --print-white: #ffffff;
    --vinyl-soft: #e6e6e6;
  }
  html, body {
    margin: 0;
    padding: 0;
    width: 1200px;
    height: 1000px;
    overflow: hidden;
    background: var(--ink-black);
  }
  .sticker-canvas {
    position: relative;
    width: 1200px;
    height: 1000px;
    background: var(--ink-black);
  }
  .sticker-art {
    position: absolute;
    inset: 0;
    width: 1200px;
    height: 1000px;
  }
  .window-frame {
    fill: none;
    stroke: var(--print-white);
    stroke-width: 1;
  }
  .floral-border {
    fill: url(#vinylTone);
  }
  .lockup-frame {
    fill: none;
    stroke: var(--print-white);
    stroke-width: 3.5;
  }
  .lockup-dot {
    fill: none;
    stroke: var(--print-white);
    stroke-width: 2;
  }
  .brand-name {
    font-family: "Marcellus", serif;
    font-weight: 400;
    font-size: 54px;
    letter-spacing: 9px;
    fill: var(--print-white);
  }
  .brand-tagline {
    font-family: "Marcellus", serif;
    font-weight: 400;
    font-size: 15px;
    letter-spacing: 0.5px;
    fill: var(--print-white);
  }
</style>
</head>
<body>
  <main class="sticker-canvas">
    <svg class="sticker-art" viewBox="0 0 1200 1000" xmlns="http://www.w3.org/2000/svg">
      <defs>
        <linearGradient id="vinylTone" x1="0" y1="0" x2="1" y2="1">
          <stop offset="0" stop-color="#ffffff"/>
          <stop offset="0.5" stop-color="#e6e6e6"/>
          <stop offset="1" stop-color="#ffffff"/>
        </linearGradient>
      </defs>

      <rect class="window-frame" x="93.5" y="147.5" width="1013" height="705"/>

      <path class="floral-border" role="img"
            aria-label="White line-art floral illustration of daisies, tulip buds, leaves and curling vines filling the right edge of the window"
            d="M850 148 L1107 148 L1107 853 L790 853
               C782 790 758 730 752 650
               C747 590 768 565 790 540
               C800 480 782 420 795 370
               C806 300 830 220 850 148 Z"/>

      <g class="brand-lockup">
        <path class="lockup-frame" d="M557 455 H444.5 V552 H543 M667 552 H756.5 V455 H645"/>
        <circle class="lockup-dot" cx="601" cy="458" r="8"/>
        <text class="brand-name" x="604" y="523" text-anchor="middle">LINDEN</text>
        <text class="brand-tagline" x="605" y="559" text-anchor="middle">Baby &amp; Spa</text>
      </g>
    </svg>
  </main>
</body>
</html>
```